Amazing Sexy Elegant Eyecatching Wine Label

We need a label designed for our wine which is going to be produced very soon.

Needs to be on a grey scale, as colours increase the price per label dramatically.

Needs to have the "Crown" logo (file attached) included on the front and back label. Logo can be in black/white but can not be changed in any way, circle around the crown must stay there as well.

We are still unsure of whether to use "Harrowby Wine" or "Harrowby" as the brand for the label, if you could submit designs based around the two names we would appreciate that.

We will have 5 varieties, including; Sauvignon Blanc, Chardonnay, Pinot Gris, Riesling and Pinot Noir. So text needs to be easily changed.

We are after an image on the label which is modern and eye catching, even in a grey scale.

Please see other attached files for an idea we have done previously, we want something a bit more "designer" though. Some information on the label is a legal requirement and needs to be kept.

Target Market(s)

Wine Consumers

Requirements
Must have
• Crown Logo, Harrowby/Harrowby Wine brand, Grey Scale, Modern Design

```html
<!DOCTYPE html>
<html lang="en">
<head>
<meta charset="utf-8">
<title>Harrowby Marlborough Sauvignon Blanc – Front and Back Label</title>
<link rel="stylesheet" href="https://fonts.googleapis.com/css2?family=Pinyon+Script&family=Sorts+Mill+Goudy:ital@0;1&family=Arimo:wght@700&family=Tinos:wght@400;700&family=Antonio:wght@200;300&display=swap">
<style>
  :root {
    --paper: #ffffff;
    --ink: #111111;
    --ink-soft: #444444;
    --ink-muted: #666666;
    --rule: #222222;
    --pattern-dark: #a6a6a6;
    --pattern-mid: #c4c4c4;
    --hill-mid: #c9c9c9;
    --hill-light: #e4e4e4;
  }
  * { box-sizing: border-box; margin: 0; padding: 0; }
  html, body { width: 1200px; height: 1000px; overflow: hidden; background: var(--paper); }
  body { position: relative; font-family: "Sorts Mill Goudy", Georgia, serif; color: var(--ink); }

  .label {
    position: absolute; top: 78px; width: 563px; height: 802px;
    border: 1.5px solid var(--rule); background: var(--paper); overflow: hidden;
  }
  .label--front { left: 13px; }
  .label--back { left: 632px; }

  .label__pattern {
    position: absolute; left: 0; top: 0; width: 100%; height: 375px;
    background: linear-gradient(to bottom,
      var(--pattern-dark) 0%,
      var(--pattern-mid) 45%,
      #dedede 72%,
      rgba(255,255,255,0) 100%);
  }
  .label__hills {
    position: absolute; left: 0; bottom: 0; width: 100%; height: 310px;
    background:
      radial-gradient(ellipse 40% 55% at 38% 38%, rgba(170,170,170,0.55), rgba(170,170,170,0) 70%),
      radial-gradient(ellipse 35% 45% at 75% 60%, rgba(170,170,170,0.45), rgba(170,170,170,0) 70%),
      linear-gradient(to bottom, rgba(255,255,255,0) 0%, var(--hill-light) 35%, var(--hill-mid) 75%, var(--hill-light) 100%);
  }
  .label--back .label__hills { opacity: 0.6; top: 500px; height: auto; }

  .brand-mark {
    position: absolute; left: 50%; top: 51px; width: 188px; height: 188px; margin-left: -94px;
    border: 2.5px solid var(--ink); border-radius: 50%; background: var(--paper);
    display: flex; align-items: center; justify-content: center;
    font-family: "Sorts Mill Goudy", Georgia, serif; font-size: 34px; color: var(--ink);
  }

  .centered { position: absolute; left: 0; width: 100%; text-align: center; }

  .brand-name { top: 283px; font-family: "Pinyon Script", cursive; font-size: 42px; color: var(--ink-soft); line-height: 1; }

  .region { top: 338px; font-family: "Arimo", Arial, sans-serif; font-weight: 700; font-size: 24px; color: var(--ink-soft); }
  .variety { top: 380px; font-family: "Tinos", "Times New Roman", serif; font-size: 31px; color: var(--ink-muted); letter-spacing: 0.5px; }
  .vintage { top: 730px; font-family: "Tinos", "Times New Roman", serif; font-size: 22px; }
  .origin { top: 768px; font-family: "Tinos", "Times New Roman", serif; font-size: 22px; }

  .tasting-note { font-size: 21px; line-height: 26.5px; color: var(--ink-soft); }
  .tasting-note--nose { top: 344px; }
  .tasting-note--pairing { top: 433px; }

  .drink-facts {
    position: absolute; left: 16px; top: 495px; width: 80px; height: 296px;
    border: 2px solid var(--ink); border-radius: 22px 22px 8px 8px; background: var(--paper);
    display: flex; flex-direction: column; align-items: center; padding-top: 86px;
  }
  .drink-facts__glass {
    width: 64px; height: 120px; background: var(--ink); border-radius: 4px 4px 30px 30px;
    color: var(--paper); font-family: "Tinos", serif; font-size: 32px; text-align: center; padding-top: 18px;
  }
  .drink-facts__abv { font-family: "Tinos", serif; font-weight: 700; font-size: 30px; line-height: 1; margin-top: 22px; }
  .drink-facts__volume { font-family: "Tinos", serif; font-weight: 700; font-size: 19px; line-height: 1.1; }

  .legal { position: absolute; left: 100px; width: 252px; text-align: center; font-family: "Antonio", "Arial Narrow", sans-serif; font-weight: 300; color: var(--ink-soft); text-transform: uppercase; line-height: 1; }
  .legal--produced { top: 582px; font-size: 19px; }
  .legal--producer { top: 605px; font-size: 11px; font-weight: 200; }
  .legal--distributed { top: 636px; font-size: 26px; }
  .legal--distributor { top: 671px; font-size: 14px; }
  .legal--responsible { top: 705px; font-size: 23px; }
  .website { position: absolute; left: 100px; width: 252px; top: 768px; text-align: center; font-size: 18px; color: var(--ink-soft); }

  .warning-badge {
    position: absolute; left: 356px; top: 575px; width: 66px; height: 66px;
    border-radius: 50%; border: 3px solid #888; background: #e6e6e6;
  }
  .partner-badge {
    position: absolute; left: 432px; top: 576px; width: 94px; height: 34px;
    border: 1.5px solid var(--ink); border-radius: 12px; background: var(--paper);
  }
  .partner-site { position: absolute; left: 432px; top: 614px; width: 110px; text-align: center; font-size: 14px; font-style: italic; color: var(--ink-soft); }
</style>
</head>
<body>

<section class="label label--front" aria-label="Front label">
  <div class="label__pattern" role="img" aria-label="Grey diamond harlequin pattern fading downward"></div>
  <div class="label__hills" role="img" aria-label="Line illustration of grey mountain ranges"></div>
  <div class="brand-mark">Harrowby</div>
  <p class="centered brand-name">Harrowby</p>
  <p class="centered region">MARLBOROUGH</p>
  <p class="centered variety">SAUVIGNON BLANC</p>
  <p class="centered vintage">2015</p>
  <p class="centered origin">WINE OF NEW ZEALAND</p>
</section>

<section class="label label--back" aria-label="Back label">
  <div class="label__pattern" role="img" aria-label="Grey diamond harlequin pattern fading downward"></div>
  <div class="label__hills" role="img" aria-label="Faint line illustration of grey mountain ranges"></div>
  <div class="brand-mark">Harrowby</div>
  <p class="centered brand-name">Harrowby</p>
  <p class="centered tasting-note tasting-note--nose">Crisp, light amber color with good acids.<br>The nose isreminiscent of freshly cut<br>herbs with a hint of mint.</p>
  <p class="centered tasting-note tasting-note--pairing">It will enhance than overpower<br>ay dish. A wonderful complement to<br>any light dish and delightly refreshing.<br>Serve lightly chilled.</p>

  <div class="drink-facts">
    <div class="drink-facts__glass">7.5</div>
    <p class="drink-facts__abv">13%</p>
    <p class="drink-facts__volume">750ml</p>
  </div>

  <p class="legal legal--produced">Produced any bottled by</p>
  <p class="legal legal--producer">Kerrigan Vale Wines | Marlborough, NZ</p>
  <p class="legal legal--distributed">Distributed by</p>
  <p class="legal legal--distributor">Harrowby Imports Ltd.</p>
  <p class="legal legal--responsible">Drink responsibily</p>
  <p class="website">www.harrowbyimports.co.nz</p>

  <div class="warning-badge" role="img" aria-label="Pregnancy alcohol warning symbol"></div>
  <div class="partner-badge" role="img" aria-label="Responsible drinking partner badge"></div>
  <p class="partner-site">sipwise.org.nz</p>
</section>

</body>
</html>
```